VALUE Book Cover Design for New Sales Book

We need a book cover designed for an upcoming book
Colors should be RED - BLACK - WHITE
A sample of our CURRENT BOOK cover (which we like) is attached
We need ideas for an "icon" or "meme" style design for the cover SIMILAR to the examples provided and attached
We need an "icon" that suggests VALUE-- we'd like the "icon" to be somewhat abstract vs using scales or anything "obvious"-- but the icon should still speak to and demonstrate what VALUE is.

Target Market(s)

Sales Directors and CEO's of large sales organizations and small businesses

Industry/Entity Type

Sales, Consulting,

Font styles to use
Sans Serif

Colors

Designer to choose colors to be used in the design.

Requirements
Must have
• Must be clean - contemporary and professional
Should not have
• should not have photos

```html
<!DOCTYPE html>
<html lang="en">
<head>
<meta charset="utf-8">
<title>Winning Worth — Book Cover</title>
<link rel="stylesheet" href="https://fonts.googleapis.com/css2?family=Bebas+Neue&family=Oswald:wght@600;700&display=swap">
<style>
  :root {
    --paper: #ffffff;
    --ink: #000000;
    --accent-red: #b90011;
    --icon-tone-a: #f1f1f1;
    --icon-tone-b: #e2e2e2;
  }
  html, body {
    margin: 0;
    padding: 0;
    overflow: hidden;
    background: var(--paper);
  }
  .cover {
    position: relative;
    width: 800px;
    height: 1200px;
    background: var(--paper);
    overflow: hidden;
  }
  .cover-icon {
    position: absolute;
    left: 256px;
    top: 51px;
    width: 285px;
    height: 291px;
    background: linear-gradient(180deg, var(--icon-tone-a), var(--icon-tone-b));
  }
  .cover-type {
    position: absolute;
    inset: 0;
    width: 800px;
    height: 1200px;
  }
  .title-main {
    font-family: "Bebas Neue", "Oswald", sans-serif;
  }
  .title-top { fill: var(--accent-red); }
  .title-bottom { fill: var(--ink); }
  .subtitle {
    font-family: "Oswald", sans-serif;
    font-weight: 600;
    fill: var(--ink);
  }
  .author {
    font-family: "Oswald", sans-serif;
    font-weight: 700;
    fill: var(--ink);
  }
  .rule-black { fill: var(--ink); }
  .rule-red { fill: var(--accent-red); }
</style>
</head>
<body>
  <main class="cover">
    <div class="cover-icon" role="img" aria-label="Line icon: a raised fist holding up a balance scale with two pans, drawn in black outline"></div>

    <svg class="cover-type" viewBox="0 0 800 1200" xmlns="http://www.w3.org/2000/svg">
      <rect class="rule-black" x="315" y="360" width="170" height="11"/>

      <text class="title-main title-top" x="98" y="592" font-size="290" textLength="604" lengthAdjust="spacingAndGlyphs">WINNING</text>
      <text class="title-main title-bottom" x="162" y="806" font-size="288" textLength="476" lengthAdjust="spacingAndGlyphs">WORTH</text>

      <rect class="rule-red" x="316" y="825" width="167" height="10"/>

      <text class="subtitle" x="172" y="900" font-size="62" textLength="455" lengthAdjust="spacingAndGlyphs">How to Close Big Deals</text>
      <text class="subtitle" x="252" y="958" font-size="62" textLength="296" lengthAdjust="spacingAndGlyphs">at Full Margin</text>

      <rect class="rule-red" x="316" y="990" width="167" height="10"/>

      <text class="author" x="183" y="1138" font-size="80" textLength="434" lengthAdjust="spacingAndGlyphs">DANA KERWIN, Ph.D</text>
    </svg>
  </main>
</body>
</html>
```